business card deign

Logo needs the following on it.
1. attached logo
2. Tagline - "If it keeps a drink cold or the party going...we do it!"
3. Name- Delia Fenwick, Founder and CPO
4. Address - 418 E. Harlow Avenue, Ste 2204, Tampa, FL. 33719
5. Phone - 720.555.0187

```html
<!DOCTYPE html>
<html lang="en">
<head>
<meta charset="utf-8">
<title>Tallow — Business Card</title>
<link href="https://fonts.googleapis.com/css2?family=Arimo:wght@400;700&family=Roboto+Condensed:wght@700&display=swap" rel="stylesheet">
<style>
  :root{
    --stage:#3b3b3b;
    --card-light:#ffffff;
    --card-dark:#262626;
    --ink:#111111;
    --ink-soft:#3a3a3a;
    --rule:#c9c9c9;
    --emboss:#4a4a4a;
    --emboss-hi:#8a8a8a;
    --web:#e6e6e6;
    --tagline:#b5b5b5;
  }
  *{box-sizing:border-box;margin:0;padding:0}
  html,body{width:1200px;height:803px;overflow:hidden;background:var(--stage)}
  .stage{
    position:relative;width:1200px;height:803px;
    display:flex;align-items:center;justify-content:center;gap:48px;
  }
  .card{
    width:520px;height:300px;border-radius:22px;position:relative;
    box-shadow:0 18px 40px rgba(0,0,0,.35);
  }
  /* front */
  .card--front{background:var(--card-light);display:flex;align-items:center;padding:0 34px}
  .brand{width:230px;display:flex;flex-direction:column;align-items:center}
  .brand__mark{width:120px;height:150px;border-radius:8px;
    background:linear-gradient(160deg,#2a2a2a,#0d0d0d)}
  .brand__name{
    margin-top:12px;font-family:"Arimo",sans-serif;font-weight:700;
    font-size:30px;letter-spacing:10px;color:var(--ink);padding-left:10px;
  }
  .divider{width:1px;height:200px;background:var(--rule);margin:0 26px}
  .contact{font-family:"Arimo",sans-serif;color:var(--ink-soft);font-size:14px;line-height:1.35}
  .contact__name{font-family:"Roboto Condensed",sans-serif;font-weight:700;font-size:21px;color:var(--ink);letter-spacing:.3px}
  .contact__role{font-size:13px;margin-bottom:14px}
  .contact__address{margin-bottom:12px}
  .contact__row{display:flex;align-items:center;gap:8px}
  .contact__row svg{width:12px;height:12px;flex:none}
  /* back */
  .card--back{background:var(--card-dark);display:flex;flex-direction:column;align-items:center;justify-content:center}
  .back__mark{width:112px;height:128px;border-radius:8px;
    background:linear-gradient(160deg,var(--emboss-hi),var(--emboss) 60%,#303030)}
  .back__name{
    margin-top:10px;font-family:"Arimo",sans-serif;font-weight:700;
    font-size:30px;letter-spacing:12px;color:var(--emboss);padding-left:12px;
  }
  .back__tagline{
    margin-top:12px;font-family:"Arimo",sans-serif;font-size:13px;
    letter-spacing:.4px;color:var(--tagline);text-align:center;max-width:440px;
  }
  .back__web{margin-top:14px;font-family:"Arimo",sans-serif;font-size:15px;letter-spacing:4px;color:var(--web)}
</style>
</head>
<body>
<main class="stage">
  <section class="card card--front">
    <div class="brand">
      <div class="brand__mark" role="img" aria-label="Brand symbol area: solid black animal silhouette"></div>
      <div class="brand__name">TALLOW</div>
    </div>
    <div class="divider"></div>
    <div class="contact">
      <p class="contact__name">DELIA FENWICK</p>
      <p class="contact__role">Founder and CPO</p>
      <p class="contact__address">418 E. Harlow Avenue<br>Ste 2204<br>Tampa, FL. 33719</p>
      <p class="contact__row">
        <svg viewBox="0 0 12 12"><path d="M2.5 1h2l1 3-1.3 1a6 6 0 0 0 2.8 2.8l1-1.3 3 1v2a1 1 0 0 1-1 1A9 9 0 0 1 1.5 2a1 1 0 0 1 1-1z" fill="#111"/></svg>
        720.555.0187
      </p>
      <p class="contact__row">
        <svg viewBox="0 0 12 12"><rect x="1" y="2.5" width="10" height="7" fill="#111"/><path d="M1 2.5l5 4 5-4" stroke="#fff" fill="none"/></svg>
        info@tallowgear.com
      </p>
      <p class="contact__row">
        <svg viewBox="0 0 12 12"><circle cx="6" cy="6" r="5" fill="#111"/><path d="M1 6h10M6 1c-2 3-2 7 0 10M6 1c2 3 2 7 0 10" stroke="#fff" stroke-width=".8" fill="none"/></svg>
        www.tallowgear.com
      </p>
    </div>
  </section>

  <section class="card card--back">
    <div class="back__mark" role="img" aria-label="Embossed brand symbol area: glossy dark animal silhouette"></div>
    <div class="back__name">TALLOW</div>
    <p class="back__tagline">If it keeps a drink cold or the party going...we do it!</p>
    <p class="back__web">www.tallowgear.com</p>
  </section>
</main>
</body>
</html>
```